We need visit card and a letter paper for our website. thx

We have a beauty clinic in Switzerland.
https://wolkenbachtal.ch
We need a visit card.

Requirements
Must have
• see colors on website

```html
<!DOCTYPE html>
<html lang="de">
<head>
<meta charset="utf-8">
<title>Wolkenbachtal – Visitenkarte</title>
<link rel="stylesheet" href="https://fonts.googleapis.com/css2?family=Lato:ital,wght@0,400;0,900;1,400&display=swap">
<style>
  :root {
    --stage: #2b2b2d;
    --brand-pink: #cf4f7e;
    --paper: #ffffff;
    --ink: #1e1e22;
    --corner-dark: #2a2526;
    --rule-pink: #e9a8c0;
  }
  * { box-sizing: border-box; margin: 0; padding: 0; }
  html, body { width: 1200px; height: 878px; overflow: hidden; }
  body {
    background: var(--stage);
    font-family: "Lato", sans-serif;
    display: flex;
    align-items: center;
    justify-content: center;
    gap: 40px;
  }
  .card {
    width: 520px;
    height: 300px;
    position: relative;
    box-shadow: 0 14px 30px rgba(0,0,0,.45);
    overflow: hidden;
  }

  /* Front side */
  .card--front { background: var(--brand-pink); color: var(--paper); }
  .card--front .brand-name {
    position: absolute;
    top: 108px; left: 0; right: 0;
    text-align: center;
    font-size: 46px;
    font-weight: 400;
    letter-spacing: 1px;
  }
  .card--front .front-url {
    position: absolute;
    bottom: 40px; left: 0; right: 0;
    text-align: center;
    font-size: 14px;
    letter-spacing: 4px;
  }

  /* Back side */
  .card--back { background: var(--paper); color: var(--ink); }
  .person { position: absolute; top: 26px; left: 32px; }
  .person__name {
    color: var(--brand-pink);
    font-weight: 900;
    font-size: 27px;
    letter-spacing: .5px;
    line-height: 1;
  }
  .person__role { font-size: 15px; margin-top: 5px; }
  .card--back .brand-name {
    position: absolute;
    top: 110px; right: 34px;
    color: var(--brand-pink);
    font-size: 32px;
    font-weight: 400;
    display: flex;
    align-items: center;
    gap: 10px;
  }
  .brand-square { width: 12px; height: 12px; background: var(--brand-pink); }
  .contacts {
    position: absolute;
    left: 30px; top: 172px;
    list-style: none;
    font-size: 15.5px;
  }
  .contacts li { display: flex; align-items: center; gap: 12px; height: 21px; }
  .contacts svg { width: 14px; height: 14px; fill: var(--brand-pink); flex: none; }
  .contacts .address {
    margin-top: 10px;
    padding-top: 6px;
    border-top: 1px solid var(--rule-pink);
    width: 460px;
  }
  .bottom-band {
    position: absolute;
    left: 52px; right: 0; bottom: 0;
    height: 18px;
    background: var(--brand-pink);
  }
  .bottom-corner {
    position: absolute;
    left: 0; bottom: 0;
    width: 46px; height: 18px;
    background: var(--corner-dark);
  }
</style>
</head>
<body>

  <section class="card card--front" aria-label="Visitenkarte Vorderseite">
    <div class="brand-name">Wolkenbachtal</div>
    <div class="front-url">www.wolkenbachtal.ch</div>
  </section>

  <section class="card card--back" aria-label="Visitenkarte Rückseite">
    <div class="person">
      <div class="person__name">LENA BRUNNER</div>
      <div class="person__role"><em>Founder &amp; CEO</em></div>
    </div>

    <div class="brand-name"><span class="brand-square"></span>Wolkenbachtal</div>

    <ul class="contacts">
      <li>
        <svg viewBox="0 0 24 24" aria-hidden="true"><path d="M6.6 10.8c1.4 2.8 3.8 5.1 6.6 6.6l2.2-2.2c.3-.3.7-.4 1-.2 1.1.4 2.3.6 3.6.6.6 0 1 .4 1 1V20c0 .6-.4 1-1 1C10.6 21 3 13.4 3 4c0-.6.4-1 1-1h3.5c.6 0 1 .4 1 1 0 1.3.2 2.5.6 3.6.1.3 0 .7-.2 1l-2.3 2.2z"/></svg>
        +41 (0) 800 24 36 48
      </li>
      <li>
        <svg viewBox="0 0 24 24" aria-hidden="true"><path d="M2 5h20v14H2zM3.5 6.5 12 13l8.5-6.5V17.5h-17z" fill-rule="evenodd"/></svg>
        hallo@wolkenbachtal.ch
      </li>
      <li>
        <svg viewBox="0 0 24 24" aria-hidden="true"><path d="M12 2a10 10 0 1 0 0 20 10 10 0 0 0 0-20zm0 2a8 8 0 0 1 0 16 8 8 0 0 1 0-16z"/><path d="M4 11h16v2H4z"/><path d="M11 4h2v16h-2z"/></svg>
        www.wolkenbachtal.ch
      </li>
      <li class="address">
        <svg viewBox="0 0 24 24" aria-hidden="true"><path d="M12 2a7 7 0 0 0-7 7c0 5 7 13 7 13s7-8 7-13a7 7 0 0 0-7-7zm0 9.5a2.5 2.5 0 1 1 0-5 2.5 2.5 0 0 1 0 5z"/></svg>
        Talweg 14, 7099 Bachwil, Switzerland
      </li>
    </ul>

    <div class="bottom-corner"></div>
    <div class="bottom-band"></div>
  </section>

</body>
</html>
```